Business Card design for Founder and CEO of new shoe company

I am looking for a business card design for my new shoe company called Strapwell.

I am launching the company this April. Strapwell shoes offers slip-on athletic and casual style shoes for men and women. The unique selling point of the brand is that all of our shoe exist without shoelaces. I have included a link to the website to offer additional information about the company, see product images, and gain inspiration for the design. You can use the store owner password "Strapwell" to access the website.

www.Strapwell.example

Thanks,
Dan Hollis

Target Market(s)

Active Men and Women ages 16-45

Industry/Entity Type

Business

Contact Information for Business Card

Dan Hollis
Founder and CEO
www.Strapwell.example
danhollis@Strapwell.example
888-555-0187 / 888-5STRAPW
Strapwell, LLC
2284 N Tamsin Ave
Chicago, IL 60699

Requirements
Must have
• Be able to quickly and easily tell that Strapwell is a shoe company from the business card

```html
<!DOCTYPE html>
<html lang="en">
<head>
<meta charset="utf-8">
<title>Strapwell Business Card</title>
<link href="https://fonts.googleapis.com/css2?family=Roboto:wght@300;400;700&display=swap" rel="stylesheet">
<style>
  :root {
    --page: #e9e7e3;
    --card-white: #ffffff;
    --card-grey: #e4e4e4;
    --ink: #111111;
    --panel: #0d0d0d;
    --panel-text: #ffffff;
    --rule: #141414;
    --shoe-pink: #e577b4;
    --shoe-cyan: #47b9dc;
    --shoe-teal: #5fd0bd;
    --shoe-navy: #34407a;
  }
  * { margin: 0; padding: 0; box-sizing: border-box; }
  html, body {
    width: 1200px; height: 892px; overflow: hidden;
    background: var(--page);
    font-family: "Roboto", Arial, sans-serif;
  }
  .canvas { position: relative; width: 1200px; height: 892px; }

  .card {
    position: absolute; left: 250px; width: 700px; height: 400px;
    overflow: hidden;
    box-shadow: 0 6px 18px rgba(0,0,0,0.18);
  }
  .card-front { top: 30px; background: var(--card-white); }
  .card-back {
    top: 462px;
    background: linear-gradient(135deg, var(--card-white) 0%, var(--card-white) 35%, var(--card-grey) 100%);
  }

  .card-shapes { position: absolute; inset: 0; }

  .brand-name {
    position: absolute; left: 40px; top: 58px;
    font-weight: 300; font-size: 64px; letter-spacing: 1px;
    color: var(--ink);
  }
  .person { position: absolute; right: 40px; top: 108px; text-align: left; }
  .person-name { font-weight: 700; font-size: 28px; color: var(--ink); }
  .person-title { font-weight: 400; font-size: 18px; color: var(--ink); margin-top: 4px; }

  .contact {
    position: absolute; right: 30px; top: 222px; width: 250px;
    color: var(--panel-text); font-size: 15px; line-height: 27px;
    text-align: right;
  }
  .contact-line { display: flex; justify-content: flex-end; align-items: center; gap: 10px; white-space: nowrap; }
  .contact-line svg { width: 12px; height: 12px; flex: none; }
  .address { margin-top: 14px; padding-right: 12px; font-size: 14px; line-height: 25px; white-space: nowrap; }
</style>
</head>
<body>
<div class="canvas">

  <section class="card card-front">
    <svg class="card-shapes" viewBox="0 0 700 400" width="700" height="400">
      <defs>
        <linearGradient id="shoeTones" x1="0" y1="1" x2="1" y2="0">
          <stop offset="0" stop-color="#ffffff"/>
          <stop offset="0.25" stop-color="#e577b4" stop-opacity="0.55"/>
          <stop offset="0.5" stop-color="#47b9dc" stop-opacity="0.6"/>
          <stop offset="0.72" stop-color="#5fd0bd" stop-opacity="0.6"/>
          <stop offset="1" stop-color="#34407a" stop-opacity="0.55"/>
        </linearGradient>
      </defs>
      <polygon class="product-photo" role="img" aria-label="Row of colourful laceless athletic shoes"
               points="0,212 376,212 420,400 0,400" fill="url(#shoeTones)"/>
      <polyline class="divider" points="0,204 382,204 392,196" fill="none" stroke="#141414" stroke-width="3"/>
      <polygon class="contact-panel" points="388,196 700,196 700,400 432,400" fill="#0d0d0d"/>
      <line class="panel-edge" x1="382" y1="206" x2="426" y2="400" stroke="#141414" stroke-width="3"/>
    </svg>

    <div class="brand-name">Strapwell</div>
    <div class="person">
      <div class="person-name">Dan Hollis</div>
      <div class="person-title">Founder and CEO</div>
    </div>

    <div class="contact">
      <div class="contact-line">888-555-0187 / 888-5STRAPW
        <svg viewBox="0 0 12 12"><path d="M2 1h3l1 3-2 1a7 7 0 0 0 3 3l1-2 3 1v3c-6 0-9-3-9-9z" fill="#fff"/></svg>
      </div>
      <div class="contact-line">danhollis@Strapwell.example
        <svg viewBox="0 0 12 12"><rect x="0.5" y="2" width="11" height="8" fill="#fff"/><path d="M0.5 2l5.5 4.5 5.5-4.5" fill="none" stroke="#0d0d0d" stroke-width="1"/></svg>
      </div>
      <div class="contact-line">www.Strapwell.example
        <svg viewBox="0 0 12 12"><circle cx="6" cy="6" r="5.5" fill="#fff"/><path d="M0.5 6h11M6 0.5c-3 3-3 8 0 11M6 0.5c3 3 3 8 0 11" fill="none" stroke="#0d0d0d" stroke-width="0.8"/></svg>
      </div>
      <div class="address">
        <div>Strapwell, LLC 2284 N Tamsin Ave</div>
        <div>Chicago, IL 60699</div>
      </div>
    </div>
  </section>

  <section class="card card-back">
    <div style="position:absolute;left:0;right:0;top:140px;text-align:center;font-weight:300;font-size:104px;letter-spacing:2px;color:var(--ink);" class="back-name">Strapwell</div>
  </section>

</div>
</body>
</html>
```